Business Card Design

Just looking for a good designs that looks good with our company logo. I'd like it to be simple and to the point. Just including contact information, our logo, and my name somewhere on the card so future clients know who they're contacting, and a couple services offered. The two images I attached are pictures of our logo. I don't care which color they they are, I just attached both images to give a reference of logo colors depending on the color of the card.
Names: Calvin Prewitt
Phone: 555-247-9061
Email: tidyturfcrew@mailvista.net
Services offered:
Mowing
Fertilization
Aeration
Bed & tree maintenance
and more.
Industry/Entity Type
Business
Contact Information for Business Card
Names: Calvin Prewitt
Phone: 555-247-9061
Look and feel

```html
<!DOCTYPE html>
<html lang="en">
<head>
<meta charset="utf-8">
<title>Tidy Turf Crew — Business Card</title>
<link href="https://fonts.googleapis.com/css2?family=Oswald:wght@500;600&family=Open+Sans:wght@400;600&display=swap" rel="stylesheet">
<style>
  :root {
    --bg-top: #e6e6e6;
    --bg-bottom: #bdbdbd;
    --card: #ffffff;
    --red: #e94b35;
    --navy: #2c3140;
    --ink: #3a3d45;
    --muted: #6b6e75;
  }
  * { margin: 0; padding: 0; box-sizing: border-box; }
  html, body { width: 1200px; height: 907px; overflow: hidden; }
  body {
    background: linear-gradient(180deg, var(--bg-top), var(--bg-bottom));
    font-family: "Open Sans", Arial, sans-serif;
    color: var(--ink);
    position: relative;
  }
  .card {
    position: absolute;
    width: 540px;
    height: 310px;
    background: var(--card);
    overflow: hidden;
    box-shadow: 0 12px 28px rgba(0,0,0,0.25);
  }
  .card--back { left: 40px; top: 298px; }
  .card--front { left: 620px; top: 298px; }
  .card__art { position: absolute; inset: 0; }

  .brand { display: flex; align-items: center; gap: 10px; }
  .brand__dot {
    width: 34px; height: 34px; border-radius: 50%;
    background: var(--red);
  }
  .brand__name {
    font-family: "Oswald", Arial, sans-serif;
    font-weight: 600;
    color: var(--navy);
    text-transform: uppercase;
    letter-spacing: 1px;
  }
  .card--back .brand {
    position: absolute; left: 50%; top: 112px; transform: translateX(-50%);
  }
  .card--back .brand__dot { width: 52px; height: 52px; }
  .card--back .brand__name { font-size: 40px; white-space: nowrap; }
  .card--back .web {
    position: absolute; right: 68px; bottom: 30px;
    font-size: 12px; color: var(--ink);
  }

  .card--front .brand { position: absolute; left: 64px; top: 58px; }
  .card--front .brand__name { font-size: 26px; white-space: nowrap; }

  .details { position: absolute; left: 250px; top: 56px; }
  .details__name {
    font-family: "Oswald", Arial, sans-serif;
    font-weight: 500; font-size: 17px; letter-spacing: 1.5px;
    text-transform: uppercase; color: var(--ink);
  }
  .details__role { font-size: 12px; color: var(--red); margin-bottom: 10px; }
  .details__address { font-size: 11px; line-height: 1.55; color: var(--muted); margin-bottom: 10px; }
  .contact { list-style: none; font-size: 11px; line-height: 1.75; color: var(--muted); }
  .contact li { display: flex; align-items: center; gap: 8px; }
  .contact svg { width: 11px; height: 11px; flex: none; }
  .contact .web { color: var(--red); }
</style>
</head>
<body>

  <section class="card card--back" aria-label="Card back">
    <svg class="card__art" viewBox="0 0 540 310" aria-hidden="true">
      <path d="M0 0 H46 C82 100 82 210 36 310 H0 Z" fill="#e94b35"/>
      <path d="M52 0 C88 100 88 210 42 310" fill="none" stroke="#2c3140" stroke-width="2"/>
      <path d="M540 0 H494 C458 100 458 210 504 310 H540 Z" fill="#e94b35"/>
      <path d="M488 0 C452 100 452 210 498 310" fill="none" stroke="#2c3140" stroke-width="2"/>
    </svg>
    <div class="brand">
      <span class="brand__dot"></span>
      <span class="brand__name">Tidy Turf Crew</span>
    </div>
    <p class="web">www.tidyturfcrew.com</p>
  </section>

  <section class="card card--front" aria-label="Card front">
    <svg class="card__art" viewBox="0 0 540 310" aria-hidden="true">
      <path d="M0 0 H330 C210 18 90 52 0 112 Z" fill="#e94b35"/>
      <path d="M340 0 C215 24 92 60 0 122" fill="none" stroke="#2c3140" stroke-width="2"/>
      <path d="M540 176 C470 244 350 290 230 310 H540 Z" fill="#e94b35"/>
      <path d="M540 166 C466 236 344 284 216 310" fill="none" stroke="#2c3140" stroke-width="2"/>
    </svg>
    <div class="brand">
      <span class="brand__dot"></span>
      <span class="brand__name">Tidy Turf</span>
    </div>
    <div class="details">
      <h1 class="details__name">Calvin Prewitt</h1>
      <p class="details__role">Managing Director</p>
      <p class="details__address">214 Meadow Row, Suite 3<br>Brookfield</p>
      <ul class="contact">
        <li><svg viewBox="0 0 12 12"><rect x="3" y="0.5" width="6" height="11" rx="1" fill="none" stroke="#e94b35" stroke-width="1.2"/></svg>555-247-9061</li>
        <li><svg viewBox="0 0 12 12"><path d="M2 1 L5 1 L6 4 L4.5 5 C5 7 6 8 7 8.5 L8 7 L11 8 L11 11 C6 11 1 6 1 2 Z" fill="#e94b35"/></svg>555-247-9061</li>
        <li><svg viewBox="0 0 12 12"><path d="M1 1 H11 V11 H1 Z" fill="none" stroke="#e94b35" stroke-width="1.2"/><path d="M3 4 H9 M3 6 H9 M3 8 H7" stroke="#e94b35"/></svg>555-247-9061</li>
        <li><svg viewBox="0 0 12 12"><rect x="0.5" y="2" width="11" height="8" fill="#e94b35"/><path d="M0.5 2 L6 7 L11.5 2" fill="none" stroke="#fff" stroke-width="1"/></svg>tidyturfcrew@mailvista.net</li>
        <li class="web"><svg viewBox="0 0 12 12"><circle cx="6" cy="6" r="5" fill="none" stroke="#e94b35" stroke-width="1.2"/><path d="M1 6 H11 M6 1 C3 4 3 8 6 11 C9 8 9 4 6 1" fill="none" stroke="#e94b35" stroke-width="0.9"/></svg>www.tidyturfcrew.com</li>
      </ul>
    </div>
  </section>

</body>
</html>
```